Bright Sweep Leaflet Campaign

We require an eye catching double sided leaflet which is for residential properties as a marketing tool to gain more business.
If you look at our website www.brightsweepgroup.com then it may help you with more information of what we are about.

We require one side of the leaflet for our (Domestic Cleaning) Services, then the other side of the leaflet for our (Carpet and Upholstery Cleaning) Service.

The Domestic Cleaning Service Side: The services we offer are weekly, fortnightly, monthly. One Off Deep Cleans. Holiday cover provided. We also have a comprehensive insurance. You may want to use our company bullet point provided in pdf which will make it stand out and outline what we do e.g.:
-Weekly, fortnightly and Monthly Cleaning Service
-Deep Blitz Cleaning
-Covered by a Comprehensive Insurance
-Carpet and Upholstery Cleaning (see overleaf)

The Carpet and Upholstery Cleaning on the other side of the leaflet has to be eye catching!

Again use bullet points along the lines of:
-Stain Removal Specialists
-Quick Drying Time
-Fresh Deodorising Finish
-Eco Friendly

Both sides of the leaflet need a call to action eg. Call Today! Our company Telephone number which should be on the leaflet in bold is 01632 960 718 .The company email which should aslo be on there is info@brightsweepuk.co.uk and the website which is not live yet is www.brightsweepuk.co.uk. If you would like to add our company accreditations they are on the website and I have attached them also.

Target Market(s)

Domestic Households- Middle aged people In York United Kingdom

Industry/Entity Type

House Cleaning

Font styles to use
Serif
Sans Serif

Requirements
Must have
• -1 Side about Domestic Cleaning Services
• -1 Side about Carpet and Upholstery Cleaning
• -Bullet points with key points
• -Phone number/website/email address
• -Logo
Nice to have
• -BE CREATIVE, USE YOUR IMAGINATION AND CREATE EYE CATCHING MATERIAL.
• -Nice to have a background colour which goes nicely with the logo our company.
Should not have
• -Not to have pink in the leaflet or yellow as it doesn't show up well I don't believe. Up to the designer as I like to give you freedom to create something amazing.

```html
<!DOCTYPE html>
<html lang="en">
<head>
<meta charset="utf-8">
<title>Bright Sweep Leaflet</title>
<link rel="stylesheet" href="https://fonts.googleapis.com/css2?family=Exo+2:wght@400;500;600&display=swap">
<style>
:root{
  --blue:#00a8df;
  --dark:#5a5656;
  --white:#ffffff;
  --ink:#333333;
  --page:#efeae4;
}
*{box-sizing:border-box;margin:0;padding:0}
html,body{width:1200px;height:1200px;overflow:hidden;background:var(--page);font-family:"Exo 2",sans-serif}
.leaflet{position:absolute;left:194px;width:812px;height:576px;background:var(--white);overflow:hidden;box-shadow:0 4px 14px rgba(0,0,0,.18)}
.front{top:12px}
.back{top:612px}
.abs{position:absolute}
.logo-box{background:var(--white);display:flex;align-items:center;justify-content:center;gap:6px;box-shadow:0 2px 6px rgba(0,0,0,.2)}
.logo-dot{width:12px;height:12px;border-radius:50%;background:var(--blue)}
.logo-name{color:var(--blue);font-weight:600;font-size:20px;line-height:1}
/* front */
.front-header{left:0;top:0;width:812px;height:116px;background:var(--dark)}
.front .logo-box{left:28px;top:0;width:136px;height:93px}
.call{color:var(--white);font-weight:500;text-align:right}
.front .call{right:36px;top:24px;font-size:20px;line-height:29px}
.phone-icon{display:inline-block;vertical-align:-3px;margin-right:5px}
.service-tab{left:260px;top:88px;width:290px;height:28px;background:var(--white);color:var(--blue);font-weight:600;font-size:18px;text-align:center;line-height:28px}
.front-photo{left:0;top:116px;width:812px;height:354px;background:linear-gradient(180deg,#f3efea 0%,#e8d9c9 30%,#d8c1a6 55%,#e9e5e2 80%,#f1f1f1 100%)}
.intro{left:40px;top:121px;width:732px;font-size:10px;line-height:13px;color:var(--ink);text-align:center}
.intro b{font-weight:600}
.card{top:175px;width:212px;height:275px;background:var(--blue);border-radius:14px;color:var(--white);text-align:center;padding-top:10px}
.card h2{font-weight:500;font-size:24px;line-height:30px}
.card .price{font-weight:500;font-size:26px;line-height:40px;margin-bottom:10px}
.card p{font-size:14px;line-height:17px}
.card .gap{height:17px}
.card.standard p{font-size:13px;line-height:20px}
.card.standard{left:62px}
.card.premium{left:298px}
.card.platinum{left:538px}
.front-footer{left:0;top:470px;width:812px;height:87px;background:var(--blue);color:var(--white)}
.foot-col{position:absolute;top:8px;font-size:13px;line-height:15px}
.foot-col h3{font-weight:600;font-size:14px;margin-bottom:3px}
.socials{display:flex;gap:6px;margin-top:6px}
.socials span{width:25px;height:25px;background:var(--white);border-radius:3px}
.badges{display:flex;gap:14px;margin-top:4px}
.badges span{width:48px;height:48px;border:2px solid var(--white);border-radius:50%}
.front-strip-white{left:0;top:557px;width:812px;height:3px;background:var(--white)}
.front-strip{left:0;top:560px;width:812px;height:16px;background:var(--dark)}
/* back */
.back-top{left:0;top:0;width:812px;height:37px;background:var(--blue)}
.back .logo-box{left:36px;top:0;width:135px;height:98px;z-index:2}
.back .call{right:16px;top:5px;font-size:20px;line-height:27px}
.back-photo{left:0;top:37px;width:812px;height:293px;background:linear-gradient(180deg,#cfd2d6 0%,#a9adb3 35%,#6f747b 65%,#4d5158 100%)}
.ribbon{left:490px;top:298px;width:322px;height:32px;background:var(--blue);color:var(--white);font-weight:600;font-size:16px;line-height:32px;padding-left:28px;clip-path:polygon(22px 0,100% 0,100% 100%,0 100%)}
.back-white-line{left:0;top:330px;width:812px;height:2px;background:var(--white)}
.back-body{left:0;top:332px;width:812px;height:220px;background:var(--dark);color:var(--white);text-align:center}
.lead{margin-top:8px;font-size:14px}
.benefits{list-style:none;margin:14px auto 0;font-size:18px;line-height:21.5px}
.benefits svg{vertical-align:-2px;margin-right:8px}
.detail{margin-top:14px;font-size:14px;line-height:16.5px}
.back-footer{left:0;top:554px;width:812px;height:22px;background:var(--blue);color:var(--white);font-weight:600;font-size:13px;line-height:22px;text-align:center}
</style>
</head>
<body>

<section class="leaflet front">
  <div class="abs front-header"></div>
  <div class="abs logo-box"><span class="logo-dot"></span><span class="logo-name">Bright Sweep</span></div>
  <div class="abs call">Call Today...!<br>
    <svg class="phone-icon" width="18" height="18" viewBox="0 0 18 18"><circle cx="9" cy="9" r="8" fill="none" stroke="#fff" stroke-width="1.6"/><path d="M6 5l2 2-1 1c.6 1.2 1.6 2.2 2.8 2.8l1-1 2 2-1.2 1.2C8.8 13 5 9.2 4.8 6.2z" fill="#fff"/></svg>01632 960 718</div>
  <div class="abs service-tab">The Domestic Cleaning Service</div>
  <div class="abs front-photo" role="img" aria-label="Softly blurred photograph of a bright, tidy home interior"></div>
  <p class="abs intro">We offer services weekly, fortnightly, monthly, one off deep cleans.  All cleans are covered by holiday cover so if the a customer has a weekly clean and the cleaner goes on holiday then it is covered. We also have a comprehensive insurance.<br><b>| Weekly,fortnightly,Monthly Cleaning | Deep Blitz Cleaning | Carpet and Upholstery Cleaning |</b></p>

  <div class="abs card standard">
    <h2>Standart</h2><div class="price">£24</div>
    <p>2hours minimum</p><p>Vacuum &amp; clean carpets &amp; floors</p><p>Dust down services</p><p>empty bins</p><p>Hygiene Clean of :</p>
    <div class="gap"></div><p>• Kitchen</p><p>• Bathroom</p><p>• Toilet</p>
  </div>
  <div class="abs card premium">
    <h2>Premium</h2><div class="price">£36</div>
    <p>As Standart Plus :</p><p>3 Hours Minimun</p><div class="gap"></div>
    <p>Interior Windows</p><div class="gap"></div>
    <p>Deep Clean :</p><p>• Kitchen</p><p>• Bathroom</p><p>• Toilet</p>
  </div>
  <div class="abs card platinum">
    <h2>Platinum</h2><div class="price">£50</div>
    <p>As Premium Plus :</p><p>4Hours Minimum</p><p>Furniture Polishing</p><div class="gap"></div>
    <p>Skirting Boards and Coving</p><p>Flowers and freshners</p>
  </div>

  <div class="abs front-footer">
    <div class="foot-col" style="left:47px"><h3>Contact :</h3>01632 960 718<br>info@brightsweepuk.co.uk<br>www.brightsweepuk.co.uk</div>
    <div class="foot-col" style="left:313px"><h3>Follow us on :</h3><div class="socials"><span></span><span></span><span></span></div></div>
    <div class="foot-col" style="left:616px"><h3 style="text-align:center">Accreditation</h3><div class="badges"><span></span><span></span></div></div>
  </div>
  <div class="abs front-strip-white"></div>
  <div class="abs front-strip"></div>
</section>

<section class="leaflet back">
  <div class="abs back-top"></div>
  <div class="abs logo-box"><span class="logo-dot"></span><span class="logo-name">Bright Sweep</span></div>
  <div class="abs call">Call Today...!
    <svg class="phone-icon" width="18" height="18" viewBox="0 0 18 18"><circle cx="9" cy="9" r="8" fill="none" stroke="#fff" stroke-width="1.6"/><path d="M6 5l2 2-1 1c.6 1.2 1.6 2.2 2.8 2.8l1-1 2 2-1.2 1.2C8.8 13 5 9.2 4.8 6.2z" fill="#fff"/></svg>01632 960 718</div>
  <div class="abs back-photo" role="img" aria-label="Photograph of a freshly mopped tiled floor with a mop, a rug and a wet floor warning sign"></div>
  <div class="abs ribbon">The Carpet and Upholstery Cleaning</div>
  <div class="abs back-white-line"></div>
  <div class="abs back-body">
    <p class="lead">The Benefit you will reap from our Domestic Carpet Cleaning Service will be paramount.</p>
    <ul class="benefits">
      <li><svg width="20" height="16" viewBox="0 0 20 16"><circle cx="9" cy="9" r="6" fill="none" stroke="#fff" stroke-width="1.2"/><path d="M5 9l3 3 9-10" fill="none" stroke="#fff" stroke-width="1.6"/></svg>Stain Removal Specialists</li>
      <li><svg width="20" height="16" viewBox="0 0 20 16"><circle cx="9" cy="9" r="6" fill="none" stroke="#fff" stroke-width="1.2"/><path d="M5 9l3 3 9-10" fill="none" stroke="#fff" stroke-width="1.6"/></svg>Quick Drying Time</li>
      <li><svg width="20" height="16" viewBox="0 0 20 16"><circle cx="9" cy="9" r="6" fill="none" stroke="#fff" stroke-width="1.2"/><path d="M5 9l3 3 9-10" fill="none" stroke="#fff" stroke-width="1.6"/></svg>Fresh Deodorising Finish</li>
      <li><svg width="20" height="16" viewBox="0 0 20 16"><circle cx="9" cy="9" r="6" fill="none" stroke="#fff" stroke-width="1.2"/><path d="M5 9l3 3 9-10" fill="none" stroke="#fff" stroke-width="1.6"/></svg>Eco Friendly</li>
    </ul>
    <p class="detail">Heavy usage or carpets can lead to carpet fibres becoming soiled, regardless of how often ypu vacuum them.<br>you will benefit from the services of our professionally trained Carpet Cleaning Staff,<br>who will help you maintain your premises to look professional and keep your carpets staying fresh<br>Tailored packages to suit your requirements.</p>
  </div>
  <div class="abs back-footer">Our Contact : 01632 960 718 | info@brightsweepuk.co.uk | www.brightsweepuk.co.uk</div>
</section>

</body>
</html>
```